Certificate of Completion - Educational Trainings

We are looking for a certificate of completion for individuals who complete one of our specific trainings. Files should be provided in a Word (docx) or PowerPoint (pptx) format. The "Talmoray example.png" file is to show necessary information. Copies of logos have been included for design purposes.

Target Market(s)

Training Participants

Industry/Entity Type

Healthcare

Font styles to use
Sans Serif

```html
<!DOCTYPE html>
<html lang="en">
<head>
<meta charset="UTF-8">
<title>Talmoray Certificate of Completion</title>
<link href="https://fonts.googleapis.com/css2?family=Poppins:wght@500;600;700&family=Roboto:ital,wght@0,400;1,400&family=Dancing+Script:wght@500;600&display=swap" rel="stylesheet">
<style>
  :root {
    --page-bg: #c4c4c4;
    --paper: #fdfdfd;
    --green: #6ab04c;
    --green-dark: #1f7a2e;
    --ornament: #8cc968;
    --ink: #1b1b1b;
    --rule: #2a2a2a;
  }
  html, body {
    margin: 0;
    padding: 0;
    width: 1199px;
    height: 1200px;
    overflow: hidden;
    background: var(--page-bg);
  }
  .certificate {
    position: absolute;
    left: 87px;
    top: 237px;
    width: 1024px;
    height: 725px;
    background: var(--paper);
    font-family: "Roboto", Arial, sans-serif;
    color: var(--ink);
  }
  .corner-ornament {
    position: absolute;
    width: 106px;
    height: 75px;
    background: linear-gradient(135deg, var(--ornament), #b9e0a3);
    opacity: 0.55;
  }
  .corner-ornament.top-left { left: 22px; top: 20px; }
  .corner-ornament.top-right { right: 22px; top: 20px; }
  .corner-ornament.bottom-left { left: 22px; bottom: 20px; }
  .corner-ornament.bottom-right { right: 22px; bottom: 20px; }
  .centered {
    position: absolute;
    left: 0;
    width: 100%;
    text-align: center;
  }
  .brand-name {
    top: 70px;
    font-family: "Poppins", Arial, sans-serif;
    font-weight: 600;
    font-size: 38px;
    letter-spacing: 2px;
    line-height: 48px;
    color: var(--ink);
  }
  .sponsor-details {
    top: 130px;
    font-size: 15px;
    line-height: 21px;
    text-transform: uppercase;
  }
  .title {
    top: 183px;
    font-family: "Poppins", Arial, sans-serif;
    font-weight: 700;
    font-size: 86px;
    line-height: 108px;
    letter-spacing: 28px;
    padding-left: 28px;
    box-sizing: border-box;
    color: var(--green);
  }
  .subtitle {
    top: 274px;
    font-family: "Dancing Script", cursive;
    font-weight: 500;
    font-size: 38px;
    line-height: 46px;
  }
  .awarded-to {
    top: 346px;
    font-size: 17px;
    letter-spacing: 3px;
    line-height: 22px;
  }
  .recipient {
    top: 383px;
    font-family: "Dancing Script", cursive;
    font-weight: 600;
    font-size: 34px;
    line-height: 42px;
    color: var(--green-dark);
  }
  .rule {
    position: absolute;
    height: 0;
    border-top: 1.5px solid var(--rule);
  }
  .rule.recipient-line { left: 262px; width: 500px; top: 431px; }
  .rule.date-line { left: 60px; width: 231px; top: 588px; }
  .rule.signature-line { left: 733px; width: 233px; top: 588px; }
  .course-details {
    top: 446px;
    font-style: italic;
    font-size: 16px;
    line-height: 20.8px;
  }
  .field-value, .field-label {
    position: absolute;
    text-align: center;
  }
  .field-value.date {
    left: 60px; width: 231px; top: 560px;
    font-size: 17px;
  }
  .field-value.signature {
    left: 733px; width: 233px; top: 544px;
    font-family: "Dancing Script", cursive;
    font-weight: 600;
    font-size: 32px;
  }
  .field-label {
    top: 603px;
    font-size: 15px;
    text-transform: uppercase;
  }
  .field-label.date { left: 60px; width: 231px; }
  .field-label.signature { left: 733px; width: 233px; }
  .seal-name {
    top: 586px;
    font-family: "Poppins", Arial, sans-serif;
    font-weight: 600;
    font-size: 22px;
    letter-spacing: 2px;
    color: var(--ink);
  }
  .accreditation-note {
    top: 650px;
    font-size: 11px;
    text-transform: uppercase;
    line-height: 14px;
  }
</style>
</head>
<body>
  <main class="certificate">
    <div class="corner-ornament top-left" role="img" aria-label="Green floral corner ornament"></div>
    <div class="corner-ornament top-right" role="img" aria-label="Green floral corner ornament"></div>
    <div class="corner-ornament bottom-left" role="img" aria-label="Green floral corner ornament"></div>
    <div class="corner-ornament bottom-right" role="img" aria-label="Green floral corner ornament"></div>

    <div class="centered brand-name">TALMORAY</div>
    <div class="centered sponsor-details">48 Harbor Lane, Ste. 310, Brinmoor, ME 04290<br>National Registry Sponsor Number 57318</div>

    <h1 class="centered title" style="margin:0">CERTIFICATE</h1>
    <div class="centered subtitle">of completion</div>

    <div class="centered awarded-to">THIS CERTIFICATE IS AWARDED TO</div>
    <div class="centered recipient">Daniel Whitcombe</div>
    <div class="rule recipient-line"></div>

    <div class="centered course-details">
      For successful completion of<br>
      Best Practices: Budget Process/Budget Building<br>
      Completed Online<br>
      Field of Study Finance<br>
      CPE Credits: 1
    </div>

    <div class="field-value date">05/16/2024</div>
    <div class="rule date-line"></div>
    <div class="field-label date">Completion Date</div>

    <div class="centered seal-name">TALMORAY</div>

    <div class="field-value signature">Clara Venn</div>
    <div class="rule signature-line"></div>
    <div class="field-label signature">Senior Consultant</div>

    <div class="centered accreditation-note">In accordance with the standard of the Central Register of CPE Providers, CPE credits have been granted based on a 50 minute hour.</div>
  </main>
</body>
</html>
```